Locksmith Business Cards

My father-in-law is in need of new business cards for his locksmith business and I need to impress him. Kindly help me out!

You can see the previous business card attached. It is a family run business in North Wales.

No individual names on the cards.

Key Things to Feature:
- The words "Prompt", "Local", "Reliable" (as you can see under the logo on the website)
- 24h Emergency Service
- Covering All of North Wales, the Wirral and Chester
- The color blue
- A key or a lock would be interesting (similar to the ones that come up when you google locksmith business card)

Optional (only if design includes bullet points, like the example below):
https://imgvaultcdnx.net/design_img/318264/57190/57190_2749031_318264_image.jpg
- Residential / Commercial / Automotive
- Alarms & Cameras
- Key Cutting & Safes

https://www.bryncoed-locksmiths-demo.co.uk/

Locksmith

01632 960 418
07700 900 362
bryncoedlocksmiths@mailvalex.com
Bryncoed Locksmiths, Hafod Barn, 4 Pennant Rd., Llandudno LL39 7QZ
www.bryncoed-locksmiths-demo.co.uk

• - The words "Prompt", "Local", "Reliable" (as you can see under the logo on the website)
• - 24h Emergency Service
• - Covering All of North Wales, the Wirral and Chester
• - A key or a lock would be interesting (similar to the ones that come up when you google locksmith business card)

```html
<!DOCTYPE html>
<html lang="en">
<head>
<meta charset="utf-8">
<title>Bryncoed Locksmiths – Business Cards</title>
<link href="https://fonts.googleapis.com/css2?family=Oswald:wght@500&family=Open+Sans:wght@400;600;700&display=swap" rel="stylesheet">
<style>
  :root {
    --navy: #262a68;
    --navy-deep: #1f2359;
    --mid-blue: #4a5ea8;
    --soft-blue: #7f8fd0;
    --paper: #ffffff;
    --stage: #e9eaee;
    --key-grey: #a9afb3;
  }
  * { box-sizing: border-box; margin: 0; padding: 0; }
  html, body { width: 1200px; height: 1021px; overflow: hidden; }
  body {
    background: var(--stage);
    font-family: "Open Sans", Arial, sans-serif;
    position: relative;
  }
  .card {
    position: absolute;
    left: 290px;
    width: 620px;
    height: 354px;
    overflow: hidden;
    box-shadow: 0 6px 18px rgba(0,0,0,.18);
  }

  /* ---------- front ---------- */
  .card-front { top: 130px; background: var(--navy); color: var(--paper); }
  .brand-row {
    position: absolute; top: 52px; left: 0; right: 0;
    display: flex; justify-content: center; align-items: center; gap: 18px;
  }
  .brand-square { width: 64px; height: 64px; background: var(--paper); border-radius: 10px; }
  .brand-name {
    font-family: "Oswald", "Arial Narrow", sans-serif;
    font-weight: 500; font-size: 46px; line-height: 1;
    text-transform: uppercase; letter-spacing: .5px; color: var(--paper);
  }
  .est-row {
    position: absolute; top: 140px; left: 120px; right: 120px;
    display: flex; align-items: center; gap: 12px;
    color: var(--soft-blue); font-size: 15px;
  }
  .est-row::before, .est-row::after {
    content: ""; flex: 1; height: 1px; background: var(--soft-blue);
  }
  .services {
    position: absolute; top: 176px; left: 0; right: 0;
    text-align: center; font-size: 17px; line-height: 23px;
  }
  .web-band {
    position: absolute; left: 0; right: 0; bottom: 24px; height: 58px;
    background: var(--mid-blue);
  }
  .web-band .web {
    position: absolute; left: 0; right: 0; top: 10px; height: 38px;
    background: var(--navy); display: flex; align-items: center; justify-content: center;
    font-weight: 700; font-size: 17px; letter-spacing: 1px;
  }

  /* ---------- back ---------- */
  .card-back { top: 534px; background: var(--paper); color: var(--navy); }
  .back-name {
    position: absolute; top: 26px; left: 40px;
    font-family: "Oswald", "Arial Narrow", sans-serif;
    font-weight: 500; font-size: 44px; line-height: 46px;
    text-transform: uppercase; color: var(--navy);
  }
  .emergency-band {
    position: absolute; top: 126px; left: 0; width: 380px; height: 36px;
    background: var(--mid-blue); color: var(--paper);
    font-weight: 700; font-size: 21px; letter-spacing: .5px;
    display: flex; align-items: center; padding-left: 40px;
  }
  .contact {
    position: absolute; top: 174px; left: 40px;
    list-style: none; font-size: 15px; line-height: 20px;
  }
  .contact li { display: flex; align-items: center; gap: 8px; }
  .contact .address { padding-left: 26px; margin-bottom: 4px; }
  .contact .phone { font-weight: 700; font-size: 21px; line-height: 27px; }
  .contact svg { width: 18px; height: 18px; flex: none; fill: none; stroke: var(--navy); stroke-width: 1.8; }
  .coverage {
    position: absolute; left: 40px; bottom: 22px;
    color: var(--mid-blue); font-size: 16px;
  }
  .motto-block {
    position: absolute; right: 40px; top: 110px;
    width: 170px; height: 170px; background: var(--navy);
    border-radius: 22px;
    display: flex; align-items: center; justify-content: center;
  }
  .motto {
    background: var(--paper); color: var(--navy);
    font-weight: 700; font-size: 21px; line-height: 25px;
    padding: 10px 14px; border-radius: 8px;
  }
</style>
</head>
<body>

<section class="card card-front" aria-label="Card front">
  <div class="brand-row">
    <span class="brand-square" aria-hidden="true"></span>
    <span class="brand-name">Bryncoed Locksmiths</span>
  </div>
  <p class="est-row">Est Since 1989</p>
  <p class="services">
    Residential / Commercial / Automotive<br>
    Alarms &amp; Cameras<br>
    Key Cutting &amp; Safes
  </p>
  <div class="web-band">
    <p class="web">www.bryncoed-locksmiths-demo.co.uk</p>
  </div>
</section>

<section class="card card-back" aria-label="Card back">
  <h1 class="back-name">Bryncoed<br>Locksmiths</h1>
  <p class="emergency-band">24h Emergency Service</p>
  <ul class="contact">
    <li class="address">Hafod Barn, 4, Pennant Rd.<br>Llandudno LL39 7QZ</li>
    <li class="phone">
      <svg viewBox="0 0 24 24" aria-hidden="true"><path d="M5 3h4l2 5-3 2a12 12 0 0 0 6 6l2-3 5 2v4a2 2 0 0 1-2 2A18 18 0 0 1 3 5a2 2 0 0 1 2-2z" fill="var(--navy)" stroke="none"/></svg>
      01632 960 418
    </li>
    <li class="phone">
      <svg viewBox="0 0 24 24" aria-hidden="true"><rect x="6" y="2" width="12" height="20" rx="2"/><line x1="10" y1="18" x2="14" y2="18"/></svg>
      07700 900 362
    </li>
    <li class="email">
      <svg viewBox="0 0 24 24" aria-hidden="true"><rect x="3" y="5" width="18" height="14"/><path d="M3 5l9 8 9-8"/></svg>
      bryncoedlocksmiths@mailvalex.com
    </li>
  </ul>
  <p class="coverage">Covering All of North Wales, the Wirral and Chester</p>
  <div class="motto-block">
    <p class="motto">Prompt.<br>Local.<br>Reliable</p>
  </div>
</section>

</body>
</html>
```